Biz Card Design BTPW

New business card for a new company.
Logo was completed by a designer on ArtFlock and looking to continue requesting additional services.
Company Name: Bright Tidal Power Works
Although this company is starting in Canada, we will be moving towards a global presence within the next 6 months.
Key elements to this business are as follows.
Energy Procurement
Energy Reduction Services
Demand Side Consulting
Energy Efficiency Consulting
Saving Clients Money
Helping Them Go "Green"
Managing Their Energy Requirements
Basically the goal for our company is to find the best procurement solution for our clients and reduce their energy consumption. This reduces their expenses and the amount of greenhouse gas they produce on a daily basis.
I have been in the energy footprint for the last 20 years and know that most companies are looking to "do whatever is necessary to get them to sign on the dotted line". I would prefer to walk away from a client that I can't help than to put them into a situation that they will regret for years to come. This is where the "BRIGHT" part of the company name comes from.
The following is a catch phrase that encompasses what we do.
"Cutting your emissions & your monthly power costs in one move!"
The back of the card needs to have this statement along with some sort of illustration. The back is a playground for creative ideas.
The front of the card needs the following.
Logo.
First & Last Name (Ned Varsolo)
Title (Power Champion)
Phone Number (555) 314-2769
Fax Number (555) 871-4420
Email Address ned@brighttidalpowerworks.example
Address 47 elmwick ave Toronto Ontario K2K 2K2
I want it to be a card that is remembered when any of my staff give it to a customer. It HAS to stand out.
Target Market(s)
Business Owners, Decision Makers, 30 to 65+
Industry/Entity Type
Business
Look and feel
Each slider illustrates characteristics of the customer's brand and the style your logo design should communicate.

```html
<!DOCTYPE html>
<html lang="en">
<head>
<meta charset="UTF-8">
<title>Bright Tidal Power Works – Business Card</title>
<link rel="stylesheet" href="https://fonts.googleapis.com/css2?family=Exo+2:wght@600&family=Arimo:wght@400;700&display=swap">
<style>
  :root {
    --stage: #e4e4e4;
    --card-black: #050505;
    --card-white: #ffffff;
    --brand-blue: #3b6fc4;
    --brand-green: #1fae4b;
    --text-light: #ffffff;
    --shadow: rgba(0, 0, 0, 0.28);
  }
  * { box-sizing: border-box; margin: 0; padding: 0; }
  html, body {
    width: 1067px;
    height: 1200px;
    overflow: hidden;
    background: var(--stage);
  }
  .stage {
    position: relative;
    width: 1067px;
    height: 1200px;
  }
  .card {
    position: absolute;
    left: 133px;
    width: 800px;
    height: 457px;
    overflow: hidden;
    box-shadow: 0 12px 30px var(--shadow);
  }

  /* Back of card */
  .card-back {
    top: 70px;
    background: var(--card-black);
  }
  .back-content {
    position: absolute;
    left: 0; right: 0;
    top: 190px;
    display: flex;
    flex-direction: column;
    align-items: center;
    gap: 22px;
  }
  .brand {
    display: flex;
    align-items: center;
    gap: 16px;
  }
  .brand-dot {
    width: 34px;
    height: 34px;
    border-radius: 50%;
    background: var(--brand-green);
    flex: none;
  }
  .brand-name {
    font-family: "Exo 2", sans-serif;
    font-weight: 600;
    color: var(--brand-blue);
    letter-spacing: -0.5px;
    white-space: nowrap;
  }
  .card-back .brand-name { font-size: 44px; }
  .tagline {
    font-family: "Arimo", sans-serif;
    font-weight: 700;
    font-size: 16px;
    color: var(--text-light);
    white-space: nowrap;
  }

  /* Front of card */
  .card-front {
    top: 660px;
    background: var(--card-black);
  }
  .front-header {
    position: absolute;
    top: 0; left: 0; right: 0;
    height: 215px;
    background: var(--card-white);
    display: flex;
    align-items: flex-end;
    justify-content: center;
    padding-bottom: 38px;
  }
  .card-front .brand-name { font-size: 42px; }
  .person {
    position: absolute;
    left: 60px;
    top: 262px;
    font-family: "Arimo", sans-serif;
    color: var(--text-light);
  }
  .person-name {
    font-family: "Exo 2", sans-serif;
    font-weight: 600;
    font-size: 30px;
    color: var(--brand-green);
    line-height: 1.1;
  }
  .person-title { font-size: 14px; margin-top: 2px; }
  .person-address { font-size: 17px; margin-top: 16px; white-space: nowrap; }
  .contacts {
    position: absolute;
    left: 455px;
    top: 236px;
    list-style: none;
    font-family: "Arimo", sans-serif;
    font-size: 15px;
    line-height: 1.45;
    color: var(--text-light);
    white-space: nowrap;
  }
  .contact-label { font-weight: 700; margin-right: 6px; }
  .label-green { color: var(--brand-green); }
  .label-blue { color: var(--brand-blue); }
  .front-stripe {
    position: absolute;
    left: 0; right: 0;
    bottom: 38px;
    height: 16px;
    display: flex;
  }
  .stripe-green { flex: 0 0 48%; background: var(--brand-green); }
  .stripe-blue { flex: 1; background: var(--brand-blue); }
</style>
</head>
<body>
<main class="stage">

  <section class="card card-back" aria-label="Card back">
    <div class="back-content">
      <div class="brand">
        <span class="brand-dot"></span>
        <span class="brand-name">BrightTidalPowerWorks</span>
      </div>
      <p class="tagline">Cutting your emissions &amp; your monthly power costs in one move!</p>
    </div>
  </section>

  <section class="card card-front" aria-label="Card front">
    <header class="front-header">
      <div class="brand">
        <span class="brand-dot"></span>
        <span class="brand-name">BrightTidalPowerWorks</span>
      </div>
    </header>

    <div class="person">
      <h1 class="person-name">Ned Varsolo</h1>
      <p class="person-title">Power Champion</p>
      <p class="person-address">47 elmwick ave Toronto Ontario K2K 2K2</p>
    </div>

    <ul class="contacts">
      <li><span class="contact-label label-green">P:</span>(555) 314-2769</li>
      <li><span class="contact-label label-blue">F:</span>(555) 871-4420</li>
      <li><span class="contact-label label-green">E:</span>ned@brighttidalpowerworks.example</li>
      <li><span class="contact-label label-blue">W:</span>www.brighttidalpowerworks.example</li>
    </ul>

    <div class="front-stripe">
      <span class="stripe-green"></span>
      <span class="stripe-blue"></span>
    </div>
  </section>

</main>
</body>
</html>
```